Builders Worksite Corflute Outdoor Sign

We are a building company who are just branching out into new construction. How first new build is our own home which was designed by us and a local architect. We are proud and want to create more advertisement around our business.

We need a corflute sign that can staked outside the construction site and can be seen by people passing by.
Updates

Can we please make the company name and logo bigger (Tidewater Ridge Homes) This needs to be the focus. Can we please replace 'Manu' with 'Contact Us on 021-574-3619'

Target Market(s)

Home owners and people wishing to build on lifestyle blocks in New Zealand.

Font styles to use
Sans Serif

Requirements
Must have
• It needs to feature our:
Logo
Company name
Contact name and number - Manu - 0215743619
Landscape NOT portrait.

```html
<!DOCTYPE html>
<html lang="en">
<head>
<meta charset="utf-8">
<title>Tidewater Ridge Homes – Site Sign</title>
<link rel="stylesheet" href="https://fonts.googleapis.com/css2?family=Jost:wght@400&family=Roboto:wght@900&family=Kanit:wght@400&display=swap">
<style>
  :root {
    --navy: #1b2333;
    --gold: #f0b919;
    --paper: #f4f4f4;
    --white: #ffffff;
  }
  html, body {
    margin: 0;
    padding: 0;
    width: 1200px;
    height: 919px;
    overflow: hidden;
    background: var(--paper);
  }
  .sign {
    display: block;
    width: 1200px;
    height: 919px;
  }
  .sign-face { fill: var(--paper); }
  .band-navy { fill: var(--navy); }
  .wedge-gold { fill: var(--gold); }
  .accent-white { fill: var(--white); }
  .stripe-gold { stroke: var(--gold); stroke-width: 5; }
  .stripe-white { stroke: var(--white); stroke-width: 5; }
  .rule { stroke: var(--white); stroke-width: 2; }
  .brand-name {
    font-family: "Jost", sans-serif;
    font-weight: 400;
    font-size: 104px;
    letter-spacing: 1px;
    fill: var(--navy);
  }
  .contact-label {
    font-family: "Kanit", sans-serif;
    font-weight: 400;
    font-size: 38px;
    fill: var(--gold);
  }
  .phone-number {
    font-family: "Roboto", sans-serif;
    font-weight: 900;
    font-size: 102px;
    fill: var(--white);
  }
  .phone-ring { fill: none; stroke: var(--white); stroke-width: 2.5; }
  .phone-handset { fill: var(--gold); }
  .phone-wave { fill: none; stroke: var(--gold); stroke-width: 3; stroke-linecap: round; }
</style>
</head>
<body>
<svg class="sign" viewBox="0 0 1200 919" xmlns="http://www.w3.org/2000/svg">
  <rect class="sign-face" x="0" y="0" width="1200" height="919"/>

  <!-- brand -->
  <text class="brand-name" text-anchor="middle">
    <tspan x="600" y="300">TIDEWATER RIDGE</tspan>
    <tspan x="600" y="430">HOMES</tspan>
  </text>

  <!-- lower graphic band -->
  <g class="band">
    <polygon class="wedge-gold" points="0,546 196,627 0,757"/>
    <polygon class="wedge-gold" points="920,605 1200,497 1200,773"/>
    <polygon class="band-navy" points="0,757 227,551 639,686 1057,524 1200,773 1200,919 0,919"/>
    <line class="stripe-gold" x1="254" y1="551" x2="544" y2="667"/>
    <line class="stripe-white" x1="845" y1="632" x2="1136" y2="530"/>
    <polygon class="accent-white" points="164,659 232,608 232,665"/>
    <polygon class="accent-white" points="1097,732 1184,778 1097,811"/>
  </g>

  <!-- contact -->
  <g class="contact">
    <line class="rule" x1="294" y1="718" x2="476" y2="718"/>
    <text class="contact-label" x="600" y="731" text-anchor="middle">Contact Us</text>
    <line class="rule" x1="722" y1="718" x2="904" y2="718"/>

    <g class="phone-icon" transform="translate(218 825)">
      <circle class="phone-ring" r="44"/>
      <path class="phone-handset" d="M-20,-18 l9,-7 l9,13 l-7,6 c3,8 8,13 16,17 l6,-7 l13,9 l-7,9 c-20,2 -41,-19 -39,-40 z"/>
      <path class="phone-wave" d="M4,-14 a12,12 0 0 1 12,12"/>
      <path class="phone-wave" d="M4,-22 a20,20 0 0 1 20,20"/>
      <path class="phone-wave" d="M4,-30 a28,28 0 0 1 28,28"/>
    </g>

    <text class="phone-number" x="655" y="864" text-anchor="middle">021-574-3619</text>
  </g>
</svg>
</body>
</html>
```